Basic images needed for business powerpoint slides

We need basic images for a powerpoint design. The designs should be clean, modern, simple and easy to read on a screen and if they were printed on paper. The images should not be overly designed (no fancy graphics or ornate fonts), but should still look professional.

Please pay attention to the attachments that have sketches of the images that are needed. In the notes section of the powerpoint slides specifies additional details for each image.

Also, please adhere to the design guidelines that are also uploaded. Only use colors and fonts that are specified. The final images should be similar to the look and feel of the images in the design guidelines.
Updates

Designers -
Thanks for all your submissions! I am reviewing all the designs with my team and will have a decision ready by Sunday evening. If you are submitting any new designs, please submit by Sunday morning EST so my team can review them.

Thanks!

Target Market(s)

business executives

Industry/Entity Type

Business

Requirements
Must have
• Must Have:
- 1. Please see the attached powerpoint for the sketches we would like to have recreated. There are specific notes in each slide with additional details.

2. Please refer to the following pages in the uploaded design guideline document:
Colors - p. 14
- Use either the bright or muted color options as specified in the color scheme on this page

Typography - p. 16-17
- Use either helvetica or arial options

Powerpoint guidelines - p.42
- see for example of the general look and feel of the company

```html
<!DOCTYPE html>
<html lang="en">
<head>
<meta charset="utf-8">
<title>Specialist Network Cycle</title>
<link href="https://fonts.googleapis.com/css2?family=Arimo:wght@400;700&display=swap" rel="stylesheet">
<style>
  :root {
    --ink: #111111;
    --muted: #8a8a8a;
    --accent-line: #f0b400;
    --page-blue: #1f4e8c;
    --bg-top: #ffffff;
    --bg-bottom: #f3f4f6;
    --footer-grey: #d9d9d9;
  }
  * { margin: 0; padding: 0; box-sizing: border-box; }
  html, body { width: 1200px; height: 844px; overflow: hidden; }
  body {
    font-family: "Arimo", Arial, Helvetica, sans-serif;
    color: var(--ink);
    background: linear-gradient(180deg, var(--bg-top) 0%, var(--bg-bottom) 100%);
  }
  .slide { position: relative; width: 1200px; height: 844px; overflow: hidden; }
  .cycle-graphic { position: absolute; left: 0; top: 0; width: 1200px; height: 844px; }

  .callout { position: absolute; }
  .callout-title { font-size: 18px; font-weight: 700; line-height: 1.2; }
  .callout-body { font-size: 13.5px; line-height: 1.4; margin-top: 24px; }
  .callout--right .callout-title { text-align: right; }

  .callout--franchise { left: 62px; top: 131px; }
  .callout--franchise .callout-body { margin-top: 26px; margin-left: -28px; width: 230px; }
  .callout--legal { left: 56px; top: 387px; }
  .callout--legal .callout-body { margin-left: -22px; width: 160px; margin-top: 26px; }
  .callout--sales { right: 57px; top: 298px; width: 300px; }
  .callout--sales .callout-body { margin-left: 62px; width: 245px; margin-top: 26px; }
  .callout--scientists { right: 115px; top: 572px; width: 330px; }
  .callout--scientists .callout-body { margin-left: 0; width: 260px; margin-top: 24px; }

  .slice-label {
    position: absolute;
    transform: translate(-50%, -50%);
    text-align: center;
    font-size: 13.5px;
    line-height: 1.2;
    color: var(--ink);
    white-space: nowrap;
  }
  .slice-label strong { font-weight: 700; display: block; }
  .slice-label--one { left: 420px; top: 310px; }
  .slice-label--two { left: 612px; top: 256px; }
  .slice-label--three { left: 706px; top: 362px; }
  .slice-label--four { left: 622px; top: 492px; }
  .slice-label--five { left: 382px; top: 485px; font-weight: 700; }

  .footer { position: absolute; left: 0; bottom: 0; width: 100%; height: 36px; }
  .page-number {
    position: absolute; left: 0; top: 0; width: 44px; height: 36px;
    background: var(--page-blue); color: #fff; font-size: 15px;
    display: flex; align-items: center; justify-content: center;
  }
  .classification {
    position: absolute; left: 44px; top: 0; width: 120px; height: 36px;
    background: linear-gradient(90deg, var(--footer-grey), #f5f5f5);
    font-size: 15px; font-weight: 700; padding-left: 26px;
    display: flex; align-items: center;
  }
  .presenter {
    position: absolute; right: 26px; top: 0; height: 36px;
    display: flex; align-items: center;
    font-size: 14px; color: var(--muted); letter-spacing: 0.3px;
  }
</style>
</head>
<body>
<main class="slide">
  <svg class="cycle-graphic" viewBox="0 0 738 519" xmlns="http://www.w3.org/2000/svg" aria-hidden="true">
    <defs>
      <linearGradient id="arrow-blue" x1="0" y1="0" x2="1" y2="0">
        <stop offset="0" stop-color="#a9c9f4"/><stop offset="1" stop-color="#3e7fd6"/>
      </linearGradient>
      <linearGradient id="arrow-orange" x1="0" y1="0" x2="0" y2="1">
        <stop offset="0" stop-color="#ffd9a3"/><stop offset="1" stop-color="#f59a2e"/>
      </linearGradient>
      <linearGradient id="arrow-purple" x1="1" y1="0" x2="0" y2="0">
        <stop offset="0" stop-color="#e4d2fa"/><stop offset="1" stop-color="#8a5fd0"/>
      </linearGradient>
      <linearGradient id="arrow-red" x1="0" y1="1" x2="0" y2="0">
        <stop offset="0" stop-color="#f7b3b3"/><stop offset="1" stop-color="#e45656"/>
      </linearGradient>
      <linearGradient id="pie-top" x1="0" y1="0" x2="1" y2="1">
        <stop offset="0" stop-color="#a8cbf6"/><stop offset="1" stop-color="#3f7fd3"/>
      </linearGradient>
      <linearGradient id="pie-side" x1="0" y1="0" x2="0" y2="1">
        <stop offset="0" stop-color="#3a6fb8"/><stop offset="1" stop-color="#173a6b"/>
      </linearGradient>
      <radialGradient id="badge" cx="0.4" cy="0.3" r="0.8">
        <stop offset="0" stop-color="#8a8a8a"/><stop offset="0.6" stop-color="#2b2b2b"/><stop offset="1" stop-color="#000"/>
      </radialGradient>
      <radialGradient id="floor-shadow" cx="0.5" cy="0.5" r="0.5">
        <stop offset="0" stop-color="#000" stop-opacity="0.55"/><stop offset="1" stop-color="#000" stop-opacity="0"/>
      </radialGradient>
      <radialGradient id="dot" cx="0.5" cy="0.5" r="0.5">
        <stop offset="0" stop-color="#f0b400"/><stop offset="0.5" stop-color="#f0b400"/><stop offset="0.6" stop-color="#fff"/><stop offset="1" stop-color="#ddd"/>
      </radialGradient>
    </defs>

    <ellipse class="floor-shadow" cx="330" cy="445" rx="150" ry="22" fill="url(#floor-shadow)"/>

    <!-- connector lines -->
    <g class="connectors" stroke="var(--accent-line)" stroke-width="1">
      <line x1="35" y1="99" x2="283" y2="99"/>
      <line x1="35" y1="256" x2="158" y2="256"/>
      <line x1="515" y1="206" x2="703" y2="206"/>
      <line x1="445" y1="374" x2="703" y2="374"/>
    </g>

    <!-- back arrows -->
    <g class="arrow arrow--red">
      <path d="M235 397.2 A190 170 0 0 1 235 102.8" fill="none" stroke="url(#arrow-red)" stroke-width="34"/>
      <polygon points="261.6,89 248.8,129.4 221.2,76.2" fill="#e45656"/>
    </g>
    <g class="arrow arrow--orange">
      <path d="M425 102.8 A190 170 0 0 1 494.5 335" fill="none" stroke="url(#arrow-orange)" stroke-width="34"/>
      <polygon points="475.5,364.4 469.3,318.7 519.7,351.3" fill="#f59a2e"/>
    </g>
    <g class="arrow arrow--blue">
      <path d="M151.4 191.9 A190 170 0 0 1 464.3 129.8" fill="none" stroke="url(#arrow-blue)" stroke-width="34"/>
      <polygon points="490,153 443,153.6 485.6,106" fill="#3e7fd6"/>
    </g>

    <!-- pie -->
    <g class="pie" stroke="#ffffff" stroke-opacity="0.5" stroke-width="0.8">
      <path d="M180.3 240.9 A155 100 0 0 1 175 215 L175 260 A155 100 0 0 0 180.3 285.9 Z" fill="url(#pie-side)"/>
      <path d="M485 215 A155 100 0 0 1 448.7 279.3 L448.7 324.3 A155 100 0 0 0 485 260 Z" fill="url(#pie-side)"/>
      <path d="M448.7 279.3 A155 100 0 0 1 303.1 313.5 L303.1 358.5 A155 100 0 0 0 448.7 324.3 Z" fill="url(#pie-side)"/>
      <path d="M330 215 L303.1 313.5 L303.1 358.5 L330 260 Z" fill="#1d4478"/>
      <path d="M330 215 L180.3 240.9 A155 100 0 0 1 330 115 Z" fill="url(#pie-top)"/>
      <path d="M330 215 L330 115 A155 100 0 0 1 475.7 180.8 Z" fill="url(#pie-top)"/>
      <path d="M330 215 L475.7 180.8 A155 100 0 0 1 448.7 279.3 Z" fill="url(#pie-top)"/>
      <path d="M330 215 L448.7 279.3 A155 100 0 0 1 303.1 313.5 Z" fill="url(#pie-top)"/>
      <g class="pie-slice--exploded" transform="translate(-24 12)">
        <path d="M303.1 313.5 A155 100 0 0 1 180.3 240.9 L180.3 285.9 A155 100 0 0 0 303.1 358.5 Z" fill="url(#pie-side)"/>
        <path d="M330 215 L303.1 313.5 A155 100 0 0 1 180.3 240.9 Z" fill="url(#pie-top)"/>
      </g>
    </g>

    <!-- front arrow -->
    <g class="arrow arrow--purple">
      <path d="M508.5 308.1 A190 170 0 0 1 184.5 359.3" fill="none" stroke="url(#arrow-purple)" stroke-width="34"/>
      <polygon points="160.5,333.8 206.4,338.8 162.6,379.8" fill="#8a5fd0"/>
    </g>

    <!-- connector dots -->
    <g class="connector-dots" fill="url(#dot)" stroke="#cfcfcf" stroke-width="0.6">
      <circle cx="283" cy="99" r="7"/>
      <circle cx="158" cy="256" r="7"/>
      <circle cx="515" cy="206" r="7"/>
      <circle cx="445" cy="374" r="7"/>
    </g>

    <!-- step badges -->
    <g class="badges" font-family="Arimo, Arial, sans-serif" font-size="17" font-weight="700" fill="#ffffff" text-anchor="middle">
      <g><circle cx="80" cy="55" r="17" fill="url(#badge)"/><text x="80" y="61">9</text></g>
      <g><circle cx="41" cy="200" r="17" fill="url(#badge)"/><text x="41" y="206">8</text></g>
      <g><circle cx="693" cy="150" r="17" fill="url(#badge)"/><text x="693" y="156">7</text></g>
      <g><circle cx="689" cy="348" r="17" fill="url(#badge)"/><text x="689" y="354">6</text></g>
      <g><circle cx="297" cy="154" r="17" fill="url(#badge)"/><text x="297" y="160">1</text></g>
      <g><circle cx="431" cy="163" r="17" fill="url(#badge)"/><text x="431" y="169">2</text></g>
      <g><circle cx="469" cy="263" r="17" fill="url(#badge)"/><text x="469" y="269">3</text></g>
      <g><circle cx="368" cy="347" r="17" fill="url(#badge)"/><text x="368" y="353">4</text></g>
      <g><circle cx="257" cy="347" r="17" fill="url(#badge)"/><text x="257" y="353">5</text></g>
    </g>
  </svg>

  <div class="slice-label slice-label--one"><strong>KVRA</strong>specialists<br>(Med Products –<br>Commercial)</div>
  <div class="slice-label slice-label--two"><strong>KVRA</strong>specialists<br>(Bio Science –<br>Commercial)</div>
  <div class="slice-label slice-label--three"><strong>KVRA</strong>specialists<br>(Med Products – Med<br>Affairs)</div>
  <div class="slice-label slice-label--four"><strong>KVRA</strong>specialists (Bio<br>Science – Med Affairs)</div>
  <div class="slice-label slice-label--five">Clinical Trials</div>

  <section class="callout callout--franchise">
    <h2 class="callout-title">Franchise Lawyers Finance</h2>
    <p class="callout-body">This is an example text. Example text. Go ahead and replace it. This is an example text.</p>
  </section>
  <section class="callout callout--legal">
    <h2 class="callout-title">Legal Analysts</h2>
    <p class="callout-body">This is an example text. Example text. Go ahead and replace it. This is an example text.</p>
  </section>
  <section class="callout callout--right callout--sales">
    <h2 class="callout-title">Sales &amp; Marketing</h2>
    <p class="callout-body">This is an example text. Example text. Go ahead and replace it. This is an example text.</p>
  </section>
  <section class="callout callout--right callout--scientists">
    <h2 class="callout-title">Scientists</h2>
    <p class="callout-body">This is an example text. Example text. Go ahead and replace it. This is an example text.</p>
  </section>

  <footer class="footer">
    <div class="page-number">8</div>
    <div class="classification">Internal</div>
    <div class="presenter">NAME OF PRESENTER</div>
  </footer>
</main>
</body>
</html>
```